BargoStreet Landing Page

We need a landing page for BargoStreet, which is a Deal of the day website targeting and providing daily deals to college students. The information we need on the page is as follows:
-The BargoStreet logo
-Save 50% to 90% on Great Deals Near Your College Campus and Beyond
-Enter Your Information
Email:
Location:
And a Submit button
-The footer
-We’d like to see a reference to how to earn credits for inviting friends: We are offering $50 Wandervane gift card for 10 new invites or $5 BargoStreet dollars for each invite.
If you visit www.bargostreet.com/marketing you can see our current landing page with all of the information. If you have any questions, please contact Renata at RCorvallo@bargostreet.com
Updates
We will need a Photoshop version of the final design as well.
BargoStreet has made a change to their target market, and is no longer just targeting college students. We are expanding our target market ages: 18-50+. The majority of our members will be between the ages of 18-35, so please keep that in mind when you are editing your designs. I am very sorry for the inconvenience. I will be extending the end date so there is enough time to edit. Thank you and keep up the great work!

```html
<!DOCTYPE html>
<html lang="en">
<head>
<meta charset="utf-8">
<title>BargoStreet – Save 50% to 90%</title>
<link rel="stylesheet" href="https://fonts.googleapis.com/css2?family=Fredoka:wght@600;700&family=Open+Sans:wght@400;600&family=Comic+Neue:wght@700&family=Arimo:wght@400;700&display=swap">
<style>
:root{
  --header-top:#3a3a3a;
  --header-bottom:#1c1c1c;
  --wood-light:#b27a4f;
  --wood-dark:#7a4a2b;
  --panel:#1f1f1f;
  --panel-edge:#2b2b2b;
  --lime:#a6cf12;
  --lime-dark:#556b10;
  --white:#ffffff;
  --muted:#cfcfcf;
  --field:#3a3a3a;
  --field-line:#555555;
  --footer:#181818;
  --footer-text:#e6e6e6;
  --divider:#3a3a3a;
  --logo-navy:#1e3445;
  --photo-tone:#8f7a68;
  --photo-tone-soft:#a38d7a;
  --mascot-tone:#6b6259;
}
*{box-sizing:border-box;margin:0;padding:0}
html,body{width:1200px;height:1151px;overflow:hidden;background:var(--footer)}
.page{position:relative;width:1200px;height:1151px;overflow:hidden}

.header{position:absolute;left:0;top:0;width:1200px;height:199px;background:linear-gradient(var(--header-top),var(--header-bottom))}
.brand{position:absolute;left:86px;top:0;width:422px;height:118px;background:var(--white);border-radius:0 0 8px 8px;box-shadow:0 3px 8px rgba(0,0,0,.5);display:flex;align-items:center;justify-content:center;gap:14px}
.brand-mark{width:26px;height:26px;background:var(--lime)}
.brand-name{font:700 50px/1 "Fredoka",sans-serif;color:var(--logo-navy)}
.headline{position:absolute;left:528px;top:26px;font:700 56px/1 "Fredoka",sans-serif;color:var(--white);text-shadow:0 2px 3px #000;white-space:nowrap}
.headline .accent{color:var(--lime)}
.headline-on{position:absolute;left:563px;top:90px;font:400 38px/1 "Open Sans",sans-serif;color:var(--white)}
.tagline{position:absolute;left:109px;top:138px;font:400 35px/1 "Open Sans",sans-serif;color:var(--white);letter-spacing:.5px;white-space:nowrap}
.mascot{position:absolute;left:985px;top:8px;width:190px;height:160px;border-radius:10px;background:linear-gradient(135deg,var(--mascot-tone),#4a4540)}

.wood{position:absolute;left:0;top:199px;width:1200px;height:693px;background:linear-gradient(90deg,var(--wood-dark),var(--wood-light) 30%,var(--wood-dark) 55%,var(--wood-light) 80%,var(--wood-dark))}
.signup{position:absolute;left:205px;top:316px;width:890px;height:396px;background:radial-gradient(ellipse at 55% 60%,var(--panel-edge),var(--panel) 70%);border:3px solid #111}
.student{position:absolute;left:151px;top:250px;width:280px;height:462px;border-radius:6px;background:linear-gradient(160deg,var(--photo-tone-soft),var(--photo-tone))}

.form-title{position:absolute;left:443px;top:354px;font:700 36px/1 "Comic Neue",cursive;color:var(--lime);letter-spacing:1.6px;white-space:nowrap}
.field-label{position:absolute;font:700 30px/1 "Comic Neue",cursive;color:var(--white);text-align:right;width:150px}
.label-email{left:447px;top:430px}
.label-location{left:450px;top:496px}
.field{position:absolute;left:637px;width:248px;height:35px;background:var(--field);border:1px solid var(--field-line)}
.field-email{top:426px}
.field-location{top:492px}
.select-arrow{position:absolute;right:2px;top:2px;width:28px;height:29px}
.submit{position:absolute;left:597px;top:570px;width:174px;height:43px;border-radius:10px;background:linear-gradient(#ffffff,#cfcfcf);font:700 30px/43px "Comic Neue",cursive;color:var(--lime-dark);text-align:center}

.invite{position:absolute;left:443px;top:638px;width:500px;font:400 15px/1.45 "Open Sans",sans-serif;color:var(--muted);text-align:center}
.invite strong{color:var(--lime);font-weight:600}

.share{position:absolute;left:961px;width:58px;height:58px}
.share-one{top:400px}
.share-two{top:480px}
.share-three{top:555px}

.footer{position:absolute;left:0;top:892px;width:1200px;height:259px;background:var(--footer)}
.footer-col{position:absolute;top:26px;font:400 15px/1 "Arimo",sans-serif;color:var(--footer-text);letter-spacing:1.3px}
.footer-col h3{font:700 15px/1 "Arimo",sans-serif;color:var(--white);margin:0 0 27px 0;letter-spacing:.8px}
.footer-col li{list-style:none;height:32px;white-space:nowrap}
.col-deal{left:230px}
.col-feedback{left:478px}
.col-faq{left:711px}
.col-legal{left:910px}
.col-faq h3{margin-left:15px}
.col-legal h3{margin-left:23px}
.divider{position:absolute;top:21px;width:1px;height:151px;background:var(--divider)}
.footer-brand{position:absolute;left:34px;top:180px;font:700 57px/1 "Arimo",sans-serif;color:#2c2c2c;white-space:nowrap}
.copyright{position:absolute;left:474px;top:199px;font:400 15px/1 "Arimo",sans-serif;color:var(--footer-text);letter-spacing:1.2px;white-space:nowrap}
</style>
</head>
<body>
<div class="page">
  <header class="header">
    <div class="brand"><span class="brand-mark"></span><span class="brand-name">BargoStreet</span></div>
    <h1 class="headline">Save <span class="accent">50%</span> To <span class="accent">90%</span></h1>
    <p class="headline-on">On</p>
    <p class="tagline">Great Deals Near Your College Campus and Beyond.</p>
    <div class="mascot" role="img" aria-label="Illustration of a graduate figure reading among stacked books"></div>
  </header>

  <main class="wood" role="img" aria-label="Vertical wood grain backdrop"></main>

  <section class="signup"></section>
  <div class="student" role="img" aria-label="Photo of a smiling young student wearing a backpack"></div>

  <h2 class="form-title">ENTER YOUR INFORMATION</h2>
  <label class="field-label label-email">Email:</label>
  <div class="field field-email"></div>
  <label class="field-label label-location">Location:</label>
  <div class="field field-location">
    <svg class="select-arrow" viewBox="0 0 28 29"><rect width="28" height="29" rx="3" fill="#222"/><path d="M11 6h6v9h5l-8 9-8-9h5z" fill="#fff"/></svg>
  </div>
  <div class="submit">Submit</div>

  <p class="invite">Invite friends and earn credits: a <strong>$50 Wandervane gift card</strong> for 10 new invites,<br>or <strong>$5 BargoStreet dollars</strong> for each invite.</p>

  <svg class="share share-one" viewBox="0 0 58 58"><rect x="10" y="10" width="38" height="38" rx="6" transform="rotate(45 29 29)" fill="#4a67a8"/></svg>
  <svg class="share share-two" viewBox="0 0 58 58"><rect x="10" y="10" width="38" height="38" rx="6" transform="rotate(45 29 29)" fill="#4bb4e0"/></svg>
  <svg class="share share-three" viewBox="0 0 58 58"><rect x="8" y="20" width="42" height="28" rx="3" fill="#e6e6e6"/><path d="M8 22l21 15 21-15" fill="none" stroke="#999" stroke-width="2"/></svg>

  <footer class="footer">
    <div class="footer-col col-deal"><h3>Daily Deal</h3><ul><li>Recent Deals</li><li>How It Works</li><li>Submit Business</li></ul></div>
    <span class="divider" style="left:404px"></span>
    <div class="footer-col col-feedback"><h3>Feedback</h3><ul><li>Sign Up</li><li>FeatureYour Business</li></ul></div>
    <span class="divider" style="left:669px"></span>
    <div class="footer-col col-faq"><h3>FAQs</h3><ul><li>About Us</li><li>Contact Us</li></ul></div>
    <span class="divider" style="left:877px"></span>
    <div class="footer-col col-legal"><h3>Legal</h3><ul><li>Our Promise</li><li>We're Hiring</li></ul></div>
    <div class="footer-brand">BargoStreet</div>
    <p class="copyright">© 2011 | BargoStreet. All Rights Reserved</p>
  </footer>
</div>
</body>
</html>
```